Solids Control Presentation Template Design

I'm putting together a technical 5-day course about solids control and waste management. I'm looking for an updated art and a easy on the eyes format.

```html
<!DOCTYPE html>
<html lang="en">
<head>
<meta charset="utf-8">
<title>Solids Control Course – Presentation Template</title>
<link href="https://fonts.googleapis.com/css2?family=Archivo+Black&family=Lato:wght@300;400;700;900&display=swap" rel="stylesheet">
<style>
:root{
  --red:#a8323a;
  --red-soft:#b5474f;
  --ink:#3b3b3b;
  --text:#6d6d6d;
  --muted:#9a9a9a;
  --grey:#bcbcbc;
  --grey-light:#dedede;
  --blue:#4f61a8;
  --page:#f2f2f2;
  --white:#ffffff;
}
*{margin:0;padding:0;box-sizing:border-box}
html,body{width:1200px;height:2201px;overflow:hidden;background:var(--page)}
body{position:relative;font-family:'Lato',sans-serif;color:var(--ink)}
.abs{position:absolute}

/* hero title slide */
.hero{position:absolute;left:70px;top:50px;width:613px;height:345px;overflow:hidden;background:var(--white)}
.hero .sky{position:absolute;inset:0;background:linear-gradient(180deg,#c9d3d9 0%,#dfe5e8 55%,#c3ccd0 100%)}
.hero .brand{position:absolute;left:0;right:0;top:150px;text-align:center}
.hero .brand .nm{font-size:40px;font-weight:900;letter-spacing:6px;color:var(--ink);line-height:40px}
.hero .brand .sub{font-size:13px;letter-spacing:3px;color:var(--red);margin-top:2px;font-variant:small-caps}
.hero .brand .svc{font-size:8.5px;font-weight:700;letter-spacing:2px;color:var(--ink);margin-top:4px}
.hero .course{position:absolute;left:0;right:0;top:233px;text-align:center;font-size:17px;font-weight:700;color:var(--red)}

/* feature list */
.features{position:absolute;left:760px;top:32px;width:440px;font-family:'Archivo Black',sans-serif;font-size:21px;color:#222;line-height:26px;list-style:none}
.features>li{position:relative;padding-left:24px;margin-bottom:4px}
.features>li::before{content:"";position:absolute;left:0;top:4px;width:17px;height:17px;border:2.5px solid #222;border-radius:2px}
.features ul{list-style:none;margin:2px 0 0 32px;font-size:19px;line-height:23px}
.features ul li{position:relative;padding-left:18px}
.features ul li::before{content:"";position:absolute;left:0;top:8px;width:7px;height:7px;background:#222}

/* slide thumbnails */
.slide{position:absolute;width:370px;height:209px;background:var(--white);overflow:hidden;box-shadow:0 3px 7px rgba(0,0,0,.3)}
.c1{left:20px}.c2{left:415px}.c3{left:809px}
.r1{top:470px}.r2{top:754px}.r3{top:1038px}.r4{top:1322px}.r5{top:1607px}.r6{top:1891px}

.logo{position:absolute;right:28px;top:12px;text-align:right}
.logo .nm{font-size:9px;font-weight:900;letter-spacing:1.5px;color:var(--ink);line-height:9px}
.logo .sub{font-size:2.8px;letter-spacing:.6px;color:var(--red);line-height:4px}
.on-dark .logo .nm,.on-dark .logo .sub{color:var(--white)}

.ttl{position:absolute;left:28px;top:19px;font-size:13px;font-weight:700;color:var(--ink);border-left:1.5px solid #555;padding-left:4px;line-height:15px;white-space:nowrap}
.ttl em{font-style:normal;color:var(--red)}
.on-dark .ttl{color:var(--white);border-color:var(--white)}

.foot{position:absolute;left:26px;top:189px;font-size:3.8px;font-weight:900;color:#222}
.rule{position:absolute;left:26px;right:20px;top:196px;height:.7px;background:var(--red)}
.pg{position:absolute;right:22px;top:188px;width:6px;height:6px;background:var(--red);color:var(--white);font-size:3.5px;text-align:center;line-height:6px}

.tiny{font-size:4.2px;line-height:7px;color:var(--text)}
.micro{font-size:3.4px;line-height:5px;color:var(--text)}
.photo{position:absolute}
.ph-rig{background:linear-gradient(135deg,#cdd6dc 0%,#4d6f7a 45%,#2f5a4e 75%,#6e7f86 100%)}
.ph-jack{background:linear-gradient(180deg,#9fb2c6 0%,#6d7f92 55%,#1f1f22 100%)}
.ph-sunset{background:linear-gradient(160deg,#f0c77a 0%,#c78a35 50%,#5a3a16 100%)}
.ph-mud{background:linear-gradient(150deg,#c8c6bd 0%,#8a8272 50%,#4e4a42 100%)}
.ph-glove{background:linear-gradient(150deg,#7b4a25 0%,#b3875a 50%,#3c2a1c 100%)}
.ph-water{background:linear-gradient(150deg,#b7a48a 0%,#6b6257 50%,#c2ad8d 100%)}
.ph-tank{background:linear-gradient(160deg,#d9dee2 0%,#6a8c96 50%,#3b5d52 100%)}

.agenda-num{position:absolute;left:45px;width:27px;height:20px;color:var(--white);font-size:9px;text-align:center;line-height:20px}
.agenda-num.red{background:var(--red)}.agenda-num.grey{background:var(--grey)}
.agenda-day{position:absolute;left:92px;font-size:5.2px;color:var(--ink)}
.bl{position:absolute;font-size:3.4px;line-height:5px;color:var(--text);padding-left:5px}
.bl::before{content:"";position:absolute;left:0;top:1.8px;width:1.6px;height:1.6px;border-radius:50%;background:var(--ink)}

.grid-item{position:absolute;width:66px;text-align:center}
.grid-item svg{display:block;margin:0 auto 4px}
.grid-item b{display:block;font-size:4.6px;color:var(--ink);font-weight:700;margin-bottom:2px}

.quote-line{position:absolute;left:150px;width:180px;border-left:.8px solid var(--muted);padding-left:5px;height:20px}
.circle{position:absolute;width:94px;height:94px;border-radius:50%;color:var(--white);text-align:center;padding-top:22px}
.circle b{display:block;font-size:5px;font-weight:400;margin-top:4px}
.circle span{display:block;font-size:3.4px;line-height:4.6px;padding:0 18px}
.element{position:absolute;width:80px;text-align:center}
.element b{display:block;font-size:4.2px;font-weight:900;color:#222;margin:4px 0 2px}
</style>
</head>
<body>

<section class="hero" aria-label="Title slide">
  <div class="sky" role="img" aria-label="Photo of an oil pumpjack silhouetted against a pale overcast sky"></div>
  <div class="brand">
    <div class="nm">KELVARD</div>
    <div class="sub">Field Process Solutions</div>
    <div class="svc">ENGINEERING • CONSULTING • TRAINING • EQUIPMENT</div>
  </div>
  <div class="course">SOLIDS CONTROL AND WASTE MANAGEMENT</div>
</section>

<ul class="features">
  <li>Ratio 16:9</li>
  <li>Full HD</li>
  <li>Custom color pallet</li>
  <li>Custom Font -&nbsp; Easy Change</li>
  <li>Easy to edit, just drag and drop images</li>
  <li>Can be included up to 100 slides;
    <ul>
      <li>Text + images (1,2,3,4) , Text Slides</li>
      <li>Portfolio Slides , blog slides</li>
      <li>Text Slides, infographics</li>
      <li>Data Slides</li>
    </ul>
  </li>
  <li>In the sample you find 19 slides</li>
</ul>

<!-- Row 1 -->
<article class="slide c1 r1">
  <div class="logo"><div class="nm">KELVARD</div><div class="sub">FIELD PROCESS SOLUTIONS</div></div>
  <div class="photo ph-jack" style="left:26px;top:54px;width:150px;height:101px" role="img" aria-label="Photo of two engineers shaking hands beside a pumpjack at dusk"></div>
  <div class="abs" style="left:185px;top:66px;width:1px;height:80px;background:#555"></div>
  <div class="abs" style="left:190px;top:65px;width:170px">
    <div style="font-size:8.5px;color:var(--ink);line-height:9px">About the Course</div>
    <div style="font-size:12.5px;font-weight:700;color:var(--red);line-height:13px">SOLIDS CONTROL AND WASTE MANAGEMENT</div>
    <p class="micro" style="margin-top:6px;width:160px">Five days of field practice on shakers, hydrocyclones and centrifuges. Learn how each stage cuts the solids load, how to read mud reports and how to plan waste handling on site so every barrel is tracked from flowline to disposal.</p>
  </div>
  <div class="foot">SOLIDS CONTROL AND WASTE MANAGEMENT</div><div class="rule"></div><div class="pg">2</div>
</article>

<article class="slide c2 r1">
  <div class="logo"><div class="nm">KELVARD</div><div class="sub">FIELD PROCESS SOLUTIONS</div></div>
  <div class="ttl">Agenda</div>
  <div class="agenda-num red" style="top:45px">01</div>
  <div class="agenda-num grey" style="top:74px">02</div>
  <div class="agenda-num red" style="top:103px">03</div>
  <div class="agenda-num grey" style="top:132px">04</div>
  <div class="agenda-num red" style="top:161px">05</div>
  <div class="agenda-day" style="top:43px">Day One</div>
  <div class="agenda-day" style="top:72px">Day Two</div>
  <div class="agenda-day" style="top:101px">Day Three</div>
  <div class="agenda-day" style="top:130px">Day Four</div>
  <div class="agenda-day" style="top:159px">Day Five</div>
  <div class="bl" style="left:92px;top:50px">Mud basics and<br>fluid roles</div>
  <div class="bl" style="left:170px;top:50px">Solids sizing, cut<br>points</div>
  <div class="bl" style="left:255px;top:50px">Shaker screens and<br>mesh choice</div>
  <div class="bl" style="left:92px;top:79px">Desander set up<br>and care</div>
  <div class="bl" style="left:170px;top:79px">Desilter cones and<br>flow rates</div>
  <div class="bl" style="left:255px;top:79px">Mud cleaner units<br>on site</div>
  <div class="bl" style="left:92px;top:108px">Centrifuge speed<br>and bowl</div>
  <div class="bl" style="left:170px;top:108px">Barite recovery<br>loops</div>
  <div class="bl" style="left:255px;top:108px">Dewatering and<br>flocculants</div>
  <div class="bl" style="left:92px;top:137px">Cuttings drying<br>methods</div>
  <div class="bl" style="left:170px;top:137px">Waste volumes<br>and logs</div>
  <div class="bl" style="left:255px;top:137px">Haul off and pit<br>closure plans</div>
  <div class="bl" style="left:92px;top:166px">Rules and field<br>permits</div>
  <div class="bl" style="left:170px;top:166px">Case studies on<br>real wells</div>
  <div class="bl" style="left:255px;top:166px">Final review and<br>assessment</div>
  <div class="foot">SOLIDS CONTROL AND WASTE MANAGEMENT</div><div class="rule"></div><div class="pg">3</div>
</article>

<article class="slide c3 r1">
  <div class="logo"><div class="nm">KELVARD</div><div class="sub">FIELD PROCESS SOLUTIONS</div></div>
  <div class="ttl">Course <em>Overview</em></div>
  <p class="tiny abs" style="left:28px;top:45px;width:318px">This course follows drilled solids from the bit to final disposal. You will see how particle size drives every equipment choice, why a clean active system cuts cost per foot, and how poor control leads to stuck pipe, lost circulation and worn pumps. Each module mixes short talks with hands-on work at a live rig site so you can test what you learn.</p>
  <p class="tiny abs" style="left:28px;top:91px;width:318px">Days two and three focus on the hardware: shaker decks, screens, hydrocyclones and decanting centrifuges. We set targets for cut points, read underflow and overflow samples, and balance flow so no unit is starved or flooded. Students build a simple solids control plan for a sample well and present it to the group.</p>
  <p class="tiny abs" style="left:28px;top:137px;width:318px">The last days cover waste: drying cuttings, treating water, storage, transport and records. You will leave with checklists, a volume calculator and a clear view of the rules that apply in your region and field.</p>
  <div class="foot">SOLIDS CONTROL AND WASTE MANAGEMENT</div><div class="rule"></div><div class="pg">4</div>
</article>

<!-- Row 2 -->
<article class="slide c1 r2">
  <div class="logo"><div class="nm">KELVARD</div><div class="sub">FIELD PROCESS SOLUTIONS</div></div>
  <div class="photo ph-tank" style="left:0;top:54px;width:143px;height:101px" role="img" aria-label="Photo of shale shakers mounted on a green mud tank"></div>
  <div class="abs" style="left:143px;top:54px;width:206px;height:101px;background:linear-gradient(90deg,rgba(168,50,58,.85),rgba(176,70,78,.95))"></div>
  <div class="abs" style="left:194px;top:70px;width:1px;height:70px;background:var(--white)"></div>
  <div class="abs" style="left:199px;top:68px;width:140px;color:var(--white)">
    <div style="font-size:15px;font-weight:700;line-height:16px">Introduction</div>
    <div style="font-size:8.5px;font-weight:700;line-height:9px">SOLIDS CONTROL AND<br>WASTE MANAGEMENT</div>
    <p class="micro" style="color:#f3dede;margin-top:4px">Why solids control matters on every well, what it costs when it fails and what you will be able to do by the end of day five.</p>
  </div>
  <div class="foot">SOLIDS CONTROL AND WASTE MANAGEMENT</div><div class="rule"></div><div class="pg">5</div>
</article>

<article class="slide c2 r2">
  <div class="logo"><div class="nm">KELVARD</div><div class="sub">FIELD PROCESS SOLUTIONS</div></div>
  <div class="ttl">Topic <em>Number One</em></div>
  <p class="tiny abs" style="left:30px;top:64px;width:150px">Drilled solids enter the mud with every foot of new hole. Fine particles raise density and viscosity, slow the rate of penetration and wear down pump liners. Removing them early, while they are still large, is cheaper than diluting the system later. This topic explains particle size ranges, how they break down as they circulate and how each unit in the line targets a band of sizes.</p>
  <div class="photo ph-sunset" style="left:193px;top:54px;width:150px;height:101px" role="img" aria-label="Photo of a pumpjack against a golden sunset sky"></div>
  <div class="foot">SOLIDS CONTROL AND WASTE MANAGEMENT</div><div class="rule"></div><div class="pg">6</div>
</article>

<article class="slide c3 r2">
  <div class="logo"><div class="nm">KELVARD</div><div class="sub">FIELD PROCESS SOLUTIONS</div></div>
  <div class="ttl">Topic <em>Number Two</em></div>
  <div class="photo ph-tank" style="left:26px;top:54px;width:150px;height:101px" role="img" aria-label="Photo of a row of shale shakers on a rig mud system"></div>
  <p class="tiny abs" style="left:195px;top:64px;width:150px">Shale shakers are the first and most important line of defence. Screen mesh, deck angle and vibration all decide how much fluid is saved and how dry the cuttings leave. This topic covers screen labels, how to spot torn panels, how to set the pool and how to log screen life so you can order the right stock before the next section starts.</p>
  <div class="foot">SOLIDS CONTROL AND WASTE MANAGEMENT</div><div class="rule"></div><div class="pg">7</div>
</article>

<!-- Row 3 -->
<article class="slide c1 r3">
  <div class="logo"><div class="nm">KELVARD</div><div class="sub">FIELD PROCESS SOLUTIONS</div></div>
  <div class="ttl" style="top:23px">Topic <em>Number Two</em></div>
  <div class="photo ph-tank" style="left:0;top:42px;width:370px;height:107px" role="img" aria-label="Wide photo of a complete solids control package on a drilling rig"></div>
  <div class="bl" style="left:38px;top:156px;font-size:4.2px;line-height:7px">Shakers remove coarse cuttings,<br>desanders take sand-size grit,<br>desilters catch the silt band</div>
  <div class="bl" style="left:124px;top:156px;font-size:4.2px;line-height:7px">centrifuges strip fine solids,<br>barite is saved and sent back,<br>clean mud returns to the pits</div>
  <div class="bl" style="left:210px;top:156px;font-size:4.2px;line-height:7px">waste is dried and measured,<br>water is treated for reuse,<br>every load is logged on site</div>
  <div class="foot">SOLIDS CONTROL AND WASTE MANAGEMENT</div><div class="rule"></div><div class="pg">8</div>
</article>

<article class="slide c2 r3 on-dark">
  <div class="abs" style="inset:0;background:linear-gradient(135deg,#8a4a55 0%,#6e2c36 55%,#4a1a22 100%)" role="img" aria-label="Photo of a pumpjack silhouette with a deep red tint"></div>
  <div class="logo"><div class="nm">KELVARD</div><div class="sub">FIELD PROCESS SOLUTIONS</div></div>
  <div class="ttl" style="top:21px">List Sample</div>
  <p class="micro abs" style="left:52px;top:50px;width:95px;color:#f0dede">Solids load is the main driver of mud cost and rig time on site.</p>
  <p class="micro abs" style="left:52px;top:76px;width:95px;color:#f0dede">Screens should be matched to the formation and the flow rate used.</p>
  <p class="micro abs" style="left:52px;top:101px;width:95px;color:#f0dede">Cone underflow should be a spray, never a rope, for best results.</p>
  <p class="micro abs" style="left:52px;top:127px;width:95px;color:#f0dede">Centrifuge feed rate must match the bowl speed and the mud weight.</p>
  <p class="micro abs" style="left:52px;top:153px;width:95px;color:#f0dede">Waste logs must show the source, volume and final place of disposal.</p>
  <svg class="abs" style="left:208px;top:56px" width="12" height="120" viewBox="0 0 12 120" fill="#fff">
    <rect x="1" y="6" width="2" height="5"/><rect x="4.5" y="3" width="2" height="8"/><rect x="8" y="0" width="2" height="11"/>
    <path d="M2 44a4 4 0 0 1 1-7 5 5 0 0 1 9 1 3 3 0 0 1 0 6z"/>
    <rect x="1" y="68" width="7" height="6" rx="1"/><path d="M8 71l4-3v6z"/>
    <circle cx="6" cy="104" r="4"/>
  </svg>
  <div class="abs" style="left:230px;top:54px;width:100px;color:#fff">
    <div style="font-size:4.6px">Statistics</div><p class="micro" style="color:#ecd2d2">Track solids content daily and plot it against the depth drilled.</p>
    <div style="font-size:4.6px;margin-top:9px">Server</div><p class="micro" style="color:#ecd2d2">Share rig reports with the office team through one shared log.</p>
    <div style="font-size:4.6px;margin-top:9px">Studio</div><p class="micro" style="color:#ecd2d2">Short video clips show each unit being set up and run safely.</p>
    <div style="font-size:4.6px;margin-top:7px">Marketing</div><p class="micro" style="color:#ecd2d2">Use clear results to show clients the value of good control.</p>
  </div>
  <div class="foot" style="color:#fff">SOLIDS CONTROL AND WASTE MANAGEMENT</div>
</article>

<article class="slide c3 r3">
  <div class="logo"><div class="nm">KELVARD</div><div class="sub">FIELD PROCESS SOLUTIONS</div></div>
  <div class="ttl">Bulletpoint <em>Topics</em></div>
  <div class="grid-item" style="left:44px;top:60px">
    <svg width="9" height="9" viewBox="0 0 10 10"><path d="M1 9l1-3 5-5 2 2-5 5z" fill="#c0392b"/></svg>
    <b>Graphic Design</b><span class="micro">Simple clear charts<br>for each field report<br>and daily summary.</span></div>
  <div class="grid-item" style="left:116px;top:60px">
    <svg width="9" height="9" viewBox="0 0 10 10"><path d="M1 4h2l3-3v8L3 6H1z" fill="#999"/></svg>
    <b>Sound Design</b><span class="micro">Noise limits near the<br>shakers and pumps<br>on a busy rig deck.</span></div>
  <div class="grid-item" style="left:186px;top:60px">
    <svg width="9" height="9" viewBox="0 0 10 10"><rect x="1" y="3" width="8" height="6" rx="1" fill="#bbb"/><circle cx="5" cy="6" r="1.6" fill="#fff"/></svg>
    <b>Photography</b><span class="micro">Photo logs of screen<br>wear and cone flow<br>for the crew files.</span></div>
  <div class="grid-item" style="left:258px;top:60px">
    <svg width="10" height="9" viewBox="0 0 10 9"><path d="M2 8a2 2 0 0 1 0-4 3 3 0 0 1 6 0 2 2 0 0 1 0 4z" fill="#4f61a8"/></svg>
    <b>Cloud Service</b><span class="micro">Shared data so the<br>office sees rig logs<br>as they are written.</span></div>
  <div class="grid-item" style="left:44px;top:118px">
    <svg width="9" height="9" viewBox="0 0 10 10"><rect x="1" y="3" width="6" height="5" fill="#c0392b"/><path d="M7 5l2-2v5z" fill="#c0392b"/></svg>
    <b>Tv Production</b><span class="micro">Training clips shot<br>on the rig floor with<br>the crew at work.</span></div>
  <div class="grid-item" style="left:116px;top:118px">
    <svg width="9" height="9" viewBox="0 0 10 10"><circle cx="5" cy="3" r="2" fill="#ddd"/><rect x="2" y="6" width="6" height="3" rx="1.5" fill="#ddd"/></svg>
    <b>Research</b><span class="micro">Field trials on new<br>screens, polymers<br>and dryer designs.</span></div>
  <div class="grid-item" style="left:186px;top:118px">
    <svg width="9" height="9" viewBox="0 0 10 10"><path d="M1 4h2l5-3v8L3 6H1z" fill="#c0392b"/></svg>
    <b>Marketing</b><span class="micro">Show clients real<br>savings per well and<br>less waste hauled.</span></div>
  <div class="grid-item" style="left:258px;top:118px">
    <svg width="9" height="9" viewBox="0 0 10 10"><rect x="1" y="2" width="8" height="6" fill="none" stroke="#bbb"/><path d="M2 7l2-2 2 2 1-1 1 1" fill="none" stroke="#bbb"/></svg>
    <b>Pictures</b><span class="micro">Clear diagrams of<br>flow paths through<br>each active tank.</span></div>
  <div class="foot">SOLIDS CONTROL AND WASTE MANAGEMENT</div><div class="rule"></div><div class="pg">10</div>
</article>

<!-- Row 4 -->
<article class="slide c1 r4">
  <div class="logo"><div class="nm">KELVARD</div><div class="sub">FIELD PROCESS SOLUTIONS</div></div>
  <div class="ttl">Talk about <em>Text&nbsp; Topic</em></div>
  <p class="tiny abs" style="left:30px;top:43px;width:152px">Hydrocyclones use the energy of the pump to spin mud inside a cone. Heavy solids move to the wall and leave at the apex, while clean fluid rises through the vortex finder. Cone size sets the cut point: larger cones take sand, smaller cones take silt. Feed head must be steady, so check the gauge each tour and keep the manifold clear of debris and rubber.<br><br>A rope discharge means the cone is overloaded and solids are being sent back to the pits. Add cones or lower the feed to restore a clean spray pattern at the apex outlet.</p>
  <p class="tiny abs" style="left:190px;top:43px;width:152px">Mud cleaners place a fine screen under the cones to save barite and liquid from the underflow stream.<br><br>Decanting centrifuges work at much higher force and can remove colloids that no screen or cone can reach. Bowl speed, pond depth and feed rate must all be set for the mud weight in use. Record each setting, sample the light and heavy streams, and compare them with the lab report before making changes on the next tour.</p>
  <div class="foot">SOLIDS CONTROL AND WASTE MANAGEMENT</div><div class="rule"></div><div class="pg">11</div>
</article>

<article class="slide c2 r4">
  <div class="logo"><div class="nm">KELVARD</div><div class="sub">FIELD PROCESS SOLUTIONS</div></div>
  <div class="ttl">Topic <em>Number</em></div>
  <p class="tiny abs" style="left:28px;top:43px;width:318px">Waste management starts at the shaker outlet. Cuttings volume, oil on cuttings and water content decide the treatment route, the storage needed and the cost of transport. Good solids control lowers every one of these numbers before the waste leaves the rig.</p>
  <p class="tiny abs" style="left:28px;top:72px;width:318px">Vertical dryers, thermal units and stabilisation each suit a different waste stream. We compare them on cost, footprint and final quality, and show how to sample, label and store each batch so the records match the load tickets.</p>
  <div class="photo ph-mud" style="left:27px;top:112px;width:101px;height:72px" role="img" aria-label="Photo of wet drill cuttings on a screen"></div>
  <div class="photo ph-glove" style="left:136px;top:112px;width:101px;height:72px" role="img" aria-label="Photo of a worker in gloves handling a sample tray"></div>
  <div class="photo ph-water" style="left:245px;top:112px;width:101px;height:72px" role="img" aria-label="Photo of a muddy water treatment pond"></div>
  <div class="foot">SOLIDS CONTROL AND WASTE MANAGEMENT</div><div class="rule"></div><div class="pg">12</div>
</article>

<article class="slide c3 r4">
  <div class="logo"><div class="nm">KELVARD</div><div class="sub">FIELD PROCESS SOLUTIONS</div></div>
  <div class="ttl">The Process <em>We talk about</em></div>
  <div class="abs" style="left:0;top:46px;width:153px;height:64px;background:var(--grey);color:#fff;text-align:center">
    <div style="font-size:8.5px;font-weight:700;margin-top:8px">Process Steps</div>
    <p class="micro" style="color:#f5f5f5;padding:3px 14px 0">Screen, separate, dry, treat and record each waste stream before it leaves the site for disposal.</p>
  </div>
  <div class="photo ph-sunset" style="left:155px;top:46px;width:70px;height:64px" role="img" aria-label="Photo of a pumpjack at sunset"></div>
  <div class="photo ph-tank" style="left:228px;top:46px;width:69px;height:64px" role="img" aria-label="Photo of shale shakers on a rig"></div>
  <div class="photo ph-mud" style="left:301px;top:46px;width:69px;height:64px" role="img" aria-label="Photo of cuttings on a screen"></div>
  <div class="abs" style="left:0;top:115px;width:80px;height:64px;background:var(--ink)"></div>
  <div class="photo ph-mud" style="left:83px;top:115px;width:70px;height:64px" role="img" aria-label="Photo of a sample being taken"></div>
  <div class="photo ph-glove" style="left:155px;top:115px;width:70px;height:64px" role="img" aria-label="Photo of a worker checking drilling fluid"></div>
  <div class="abs" style="left:228px;top:115px;width:69px;height:64px;background:var(--blue);color:#fff">
    <div style="position:absolute;left:4px;top:6px;font-size:11px;font-weight:900">“</div>
    <p class="micro" style="color:#e6e9f5;padding:8px 6px 0 16px">Clean mud is the cheapest mud. Every solid left in the system costs time and money.</p>
  </div>
  <div class="photo ph-jack" style="left:301px;top:115px;width:69px;height:64px" role="img" aria-label="Photo of engineers beside a pumpjack"></div>
  <div class="foot">SOLIDS CONTROL AND WASTE MANAGEMENT</div><div class="rule"></div><div class="pg">13</div>
</article>

<!-- Row 5 -->
<article class="slide c1 r5">
  <div class="logo"><div class="nm">KELVARD</div><div class="sub">FIELD PROCESS SOLUTIONS</div></div>
  <div class="ttl">Text and <em>Bullets</em></div>
  <p class="tiny abs" style="left:28px;top:43px;width:318px">Every rig needs a written solids control plan. It lists the equipment on site, the target cut point for each unit, the screen stock on hand and the checks made each tour. It also sets limits for low gravity solids and the action taken when a limit is passed.</p>
  <p class="tiny abs" style="left:28px;top:72px;width:318px">A good plan is short, clear and kept at the shaker house where the crew can see it.</p>
  <div class="quote-line" style="top:97px"><p class="micro">Check screens for tears at every connection and log each change made.</p></div>
  <div class="quote-line" style="top:126px"><p class="micro">Keep cone feed pressure steady and watch the underflow for roping.</p></div>
  <div class="quote-line" style="top:154px"><p class="micro">Sample waste streams daily and match them to the haul off tickets.</p></div>
  <div class="foot">SOLIDS CONTROL AND WASTE MANAGEMENT</div><div class="rule"></div><div class="pg">14</div>
</article>

<article class="slide c2 r5">
  <div class="logo"><div class="nm">KELVARD</div><div class="sub">FIELD PROCESS SOLUTIONS</div></div>
  <div class="ttl">Analytics <em>Three Facts</em></div>
  <div class="abs" style="left:28px;top:56px;font-size:4.8px;font-weight:700;color:#222">Analysis of the Chart</div>
  <p class="tiny abs" style="left:28px;top:64px;width:150px">Solids content rises fast when the shakers run with worn screens. The chart compares four wells: the red area shows low gravity solids and the grey area shows total solids. Wells with a full centrifuge program kept solids far lower through the deep section and used less dilution, less barite and less disposal space at the end of the job.</p>
  <svg class="abs" style="left:190px;top:58px" width="165" height="100" viewBox="0 0 165 100">
    <g font-family="Lato,sans-serif" font-size="5" fill="#777">
      <text x="2" y="6">6</text><text x="2" y="18">5</text><text x="2" y="30">4</text><text x="2" y="42">3</text><text x="2" y="54">2</text><text x="2" y="66">1</text><text x="2" y="78">0</text>
      <text x="12" y="88">Category 1</text><text x="47" y="88">Category 2</text><text x="87" y="88">Category 3</text><text x="127" y="88">Category 4</text>
    </g>
    <path d="M12 76V40L32 60L52 54L72 62L92 54L152 24V76Z" fill="var(--red)"/>
    <path d="M12 76V54L52 30L92 54L132 42L152 36V76Z" fill="#c4c4c4"/>
  </svg>
  <div class="foot">SOLIDS CONTROL AND WASTE MANAGEMENT</div><div class="rule"></div><div class="pg">15</div>
</article>

<article class="slide c3 r5">
  <div class="logo"><div class="nm">KELVARD</div><div class="sub">FIELD PROCESS SOLUTIONS</div></div>
  <div class="ttl">Analytics <em>Three Facts</em></div>
  <svg class="abs" style="left:28px;top:70px" width="160" height="80" viewBox="0 0 160 80">
    <g font-family="Lato,sans-serif" font-size="5" fill="#777">
      <text x="0" y="7">Category 4</text><text x="0" y="26">Category 3</text><text x="0" y="45">Category 2</text><text x="0" y="64">Category 1</text>
      <text x="33" y="78">0%</text><text x="49" y="78">20%</text><text x="69" y="78">40%</text><text x="90" y="78">60%</text><text x="111" y="78">80%</text><text x="131" y="78">100%</text>
    </g>
    <rect x="43" y="2" width="106" height="6" fill="#e3e3e3"/><rect x="43" y="2" width="66" height="6" fill="#c8c8c8"/><rect x="43" y="2" width="39" height="6" fill="var(--red)"/>
    <rect x="43" y="21" width="106" height="6" fill="#e3e3e3"/><rect x="43" y="21" width="73" height="6" fill="#c8c8c8"/><rect x="43" y="21" width="46" height="6" fill="var(--red)"/>
    <rect x="43" y="40" width="106" height="6" fill="#e3e3e3"/><rect x="43" y="40" width="64" height="6" fill="#c8c8c8"/><rect x="43" y="40" width="29" height="6" fill="var(--red)"/>
    <rect x="43" y="59" width="106" height="6" fill="#e3e3e3"/><rect x="43" y="59" width="76" height="6" fill="#c8c8c8"/><rect x="43" y="59" width="53" height="6" fill="var(--red)"/>
  </svg>
  <div class="abs" style="left:208px;top:78px;width:140px">
    <div style="position:relative;height:28px"><span class="abs" style="left:0;top:0;width:16px;height:16px;border-radius:50%;background:var(--red)"></span><div class="abs" style="left:24px;top:0"><div style="font-size:4.2px;font-weight:700;color:#222">Factor Number One</div><p class="micro">Low gravity solids fell<br>by half on two wells.</p></div></div>
    <div style="position:relative;height:28px"><span class="abs" style="left:0;top:0;width:16px;height:16px;border-radius:50%;background:#9a9a9a"></span><div class="abs" style="left:24px;top:0"><div style="font-size:4.2px;font-weight:700;color:#222">Factor Number Two</div><p class="micro">Dilution volume dropped<br>with fine screens.</p></div></div>
    <div style="position:relative;height:28px"><span class="abs" style="left:0;top:0;width:16px;height:16px;border-radius:50%;background:#c8c8c8"></span><div class="abs" style="left:24px;top:0"><div style="font-size:4.2px;font-weight:700;color:#222">Factor Number Three</div><p class="micro">Waste hauled per well<br>was cut by a third.</p></div></div>
  </div>
  <div class="foot">SOLIDS CONTROL AND WASTE MANAGEMENT</div><div class="rule"></div><div class="pg">16</div>
</article>

<!-- Row 6 -->
<article class="slide c1 r6">
  <div class="logo"><div class="nm">KELVARD</div><div class="sub">FIELD PROCESS SOLUTIONS</div></div>
  <div class="ttl">Infographic <em style="color:var(--ink)">Slides</em></div>
  <div class="circle" style="left:19px;top:52px;background:rgba(176,176,176,.9)">
    <svg width="14" height="11" viewBox="0 0 14 11"><rect x="1" y="2" width="12" height="8" rx="1" fill="none" stroke="#fff" stroke-width="1.2"/><circle cx="7" cy="6" r="2" fill="none" stroke="#fff"/></svg>
    <b>Photography</b><span>Photo logs of screens and cones for the daily report.</span></div>
  <div class="circle" style="left:96px;top:52px;background:rgba(196,196,196,.85)">
    <svg width="14" height="11" viewBox="0 0 14 11"><rect x="1" y="1" width="12" height="9" fill="none" stroke="#fff" stroke-width="1.2"/><path d="M7 8V4M5 6l2-2 2 2" fill="none" stroke="#fff"/></svg>
    <b>Web Server</b><span>Rig data sent to the office for review.</span></div>
  <div class="circle" style="left:179px;top:52px;background:rgba(79,97,168,.92)">
    <svg width="14" height="12" viewBox="0 0 14 12"><path d="M2 11L11 2M3 2l9 9" stroke="#fff" stroke-width="1.6"/></svg>
    <b>Web Design</b><span>Simple tools to log and plot solids data.</span></div>
  <div class="circle" style="left:258px;top:52px;background:rgba(205,60,68,.92)">
    <svg width="14" height="12" viewBox="0 0 14 12"><path d="M2 4h3l6-3v10L5 8H2z" fill="#fff"/></svg>
    <b>Promotion</b><span>Share results and savings with clients.</span></div>
  <p class="tiny abs" style="left:28px;top:154px;width:318px">Four support areas help the crew keep records clean and useful. Photos, shared data, simple tools and clear reporting turn daily rig work into lessons the next well can use.</p>
  <div class="foot">SOLIDS CONTROL AND WASTE MANAGEMENT</div><div class="rule"></div><div class="pg">17</div>
</article>

<article class="slide c2 r6">
  <div class="logo"><div class="nm">KELVARD</div><div class="sub">FIELD PROCESS SOLUTIONS</div></div>
  <div class="ttl">Elements <em>Comparison Chart</em></div>
  <svg class="abs" style="left:0;top:52px" width="370" height="72" viewBox="0 0 370 72">
    <g fill="none" stroke-width="2">
      <circle cx="64" cy="35" r="31" stroke="var(--blue)"/><path d="M64 4a31 31 0 0 1 28 18" stroke="var(--red)"/>
      <circle cx="143" cy="35" r="31" stroke="var(--blue)"/><path d="M143 4a31 31 0 0 1 31 31" stroke="var(--red)"/>
      <circle cx="231" cy="35" r="31" stroke="var(--blue)"/><path d="M231 4a31 31 0 0 1 26 14" stroke="var(--red)"/>
      <circle cx="310" cy="35" r="31" stroke="var(--blue)"/><path d="M310 4a31 31 0 0 1 22 9" stroke="var(--red)"/>
    </g>
    <circle cx="64" cy="35" r="8" fill="var(--red)"/>
    <circle cx="143" cy="35" r="8" fill="#9a9a9a"/>
    <circle cx="231" cy="35" r="8" fill="#9a9a9a"/>
    <circle cx="310" cy="35" r="8" fill="var(--blue)"/>
  </svg>
  <div class="element" style="left:24px;top:128px"><b>ELEMENT ONE</b><p class="micro">Shakers save most fluid<br>at the lowest cost.</p></div>
  <div class="element" style="left:103px;top:128px"><b>ELEMENT TWO</b><p class="micro">Cones take sand and<br>silt in one pass.</p></div>
  <div class="element" style="left:191px;top:128px"><b>ELEMENT THREE</b><p class="micro">Mud cleaners save<br>barite from underflow.</p></div>
  <div class="element" style="left:270px;top:128px"><b>ELEMENT FOUR</b><p class="micro">Centrifuges reach the<br>finest colloid band.</p></div>
  <p class="micro abs" style="left:28px;top:165px;width:318px">Each element is rated on cut point, cost and fluid saved. The red arc shows its share of total solids removed across the sample wells in this course.</p>
  <div class="foot">SOLIDS CONTROL AND WASTE MANAGEMENT</div><div class="rule"></div><div class="pg">18</div>
</article>

<article class="slide c3 r6">
  <div class="abs" style="inset:0;background:linear-gradient(160deg,#2f6fb0 0%,#7aa7d6 35%,#c46a2a 60%,#e9a24d 100%)" role="img" aria-label="Photo of an orange drilling rig derrick against a blue sky"></div>
  <div class="abs" style="left:0;top:133px;width:370px;height:48px;background:rgba(168,50,58,.85)"></div>
  <div class="abs" style="left:36px;top:146px;width:1.5px;height:22px;background:#fff"></div>
  <div class="abs" style="left:42px;top:148px;font-size:13px;font-weight:700;color:#fff">Break Time</div>
</article>

</body>
</html>
```